We have developed a fully functional App called Harborwink. However, it requires a nicer GUI. You can see screenshots of our App on www.harborwink-example.com under "Tutorial". For those of you with Android, you can also install it. When you go to Harborwink-example.com, your phone will automatically redirect you to download. From there, you'll get a better idea of what our App looks like and how your design can make it way better. Please note we expect a design idea for most screens (there's about 8 screens) but do just one screen first and if you win, you can do the other 8 after.

Target Market(s)

People looking for dating / flirting

Industry/Entity Type

Android

Requirements
Must have
• sleek looking

```html
<!DOCTYPE html>
<html lang="en">
<head>
<meta charset="utf-8">
<title>Harborwink – App Screens</title>
<link href="https://fonts.googleapis.com/css2?family=Open+Sans:wght@400;600;700&display=swap" rel="stylesheet">
<style>
  :root {
    --page-bg: #e8edef;
    --header-blue: #1f5d8c;
    --header-dark: #17476d;
    --header-active: #2a6d9e;
    --sky-top: #8fd0ec;
    --sky-mid: #95b9e2;
    --sky-bottom: #8a86c9;
    --bubble: #ffffff;
    --name-blue: #1d4f86;
    --age-pink: #c4127a;
    --online: #3cb54a;
    --body-text: #333333;
    --location: #ffffff;
    --field-bg: #eeeeee;
    --field-bg-active: #ffffff;
    --field-text: #8a8a8a;
    --field-text-active: #333333;
    --arrow: #666666;
    --tab-pink: #c8107e;
    --tab-deep: #a50c69;
    --ring-pink: #c3147e;
    --ring-blue: #2f6fb0;
    --status-bg: #1a1a1a;
    --placeholder: #d9d9d9;
    --silhouette: #6d6d6d;
  }
  * { box-sizing: border-box; margin: 0; padding: 0; }
  html, body {
    width: 1200px; height: 991px; overflow: hidden;
    background: var(--page-bg);
    font-family: "Open Sans", Arial, sans-serif;
  }
  .screen {
    position: absolute; top: 135px; width: 460px; height: 720px;
    overflow: hidden;
    background: linear-gradient(180deg, var(--sky-top) 0%, var(--sky-mid) 50%, var(--sky-bottom) 100%);
    box-shadow: 0 10px 30px rgba(0,0,0,.18);
  }
  .screen--inbox { left: 110px; }
  .screen--profile { left: 630px; }

  .status-bar {
    height: 30px; background: var(--status-bg); color: #fff;
    display: flex; align-items: center; justify-content: space-between;
    padding: 0 12px; font-size: 15px; font-weight: 600;
  }
  .status-bar .carrier { display: flex; align-items: center; gap: 6px; font-size: 13px; }
  .status-bar .battery { width: 30px; height: 13px; border: 2px solid #fff; border-radius: 3px; position: relative; }
  .status-bar .battery::after { content: ""; position: absolute; inset: 1px; background: #fff; }

  .app-header {
    height: 86px; display: flex; align-items: stretch;
    background: linear-gradient(180deg, var(--header-blue), var(--header-dark));
  }
  .brand {
    flex: 1; display: flex; align-items: center; gap: 10px; padding-left: 20px;
    color: #fff; font-size: 24px; font-weight: 600;
  }
  .brand-dot { width: 22px; height: 22px; border-radius: 50%; background: #fff; }
  .nav-item {
    width: 86px; display: flex; align-items: center; justify-content: center;
    border-left: 1px solid rgba(0,0,0,.2);
  }
  .nav-item--active { background: var(--header-dark); }
  .nav-item--lit { background: var(--header-active); }

  /* Inbox list */
  .thread-list { list-style: none; padding: 30px 0 0 20px; }
  .thread { display: flex; align-items: flex-start; height: 160px; }
  .avatar-col { width: 110px; text-align: center; }
  .avatar {
    width: 98px; height: 98px; border-radius: 50%;
    border: 4px solid var(--ring-pink); box-shadow: inset 0 0 0 3px #fff;
    background: radial-gradient(circle at 50% 40%, #e8c7b2 0%, #a98170 60%, #5a4038 100%);
  }
  .avatar--blue { border-color: var(--ring-blue); }
  .location { display: block; margin-top: 8px; color: var(--location); font-size: 12px; }
  .bubble {
    position: relative; margin-left: 26px; width: 290px; min-height: 104px;
    background: var(--bubble); padding: 12px 14px; margin-top: 6px;
    box-shadow: 0 2px 4px rgba(0,0,0,.15);
  }
  .bubble::before {
    content: ""; position: absolute; left: -14px; top: 18px;
    border-style: solid; border-width: 10px 14px 10px 0;
    border-color: transparent var(--bubble) transparent transparent;
  }
  .bubble-name { font-size: 17px; font-weight: 700; color: var(--name-blue); display: flex; align-items: center; gap: 8px; }
  .online-dot { width: 10px; height: 10px; border-radius: 50%; background: var(--online); }
  .bubble-age { color: var(--age-pink); }
  .bubble-text { margin-top: 6px; font-size: 15px; line-height: 1.35; color: var(--body-text); }

  /* Profile form */
  .profile-form { padding: 36px 44px 0; display: flex; flex-direction: column; gap: 9px; }
  .field {
    height: 62px; background: var(--field-bg); display: flex; align-items: center;
    justify-content: space-between; padding: 0 18px; font-size: 20px; color: var(--field-text);
  }
  .field--active { background: var(--field-bg-active); color: var(--field-text-active); }
  .field-row { display: flex; gap: 8px; }
  .field--age { width: 102px; }
  .field--sex { flex: 1; }
  .arrow { width: 0; height: 0; border-style: solid; border-width: 12px 8px 0 8px; border-color: var(--arrow) transparent transparent transparent; }
  .pics-label { margin-top: 20px; color: #fff; font-size: 19px; }
  .pic-row { display: flex; gap: 7px; }
  .pic { width: 88px; height: 88px; background: var(--placeholder); display: flex; align-items: flex-end; justify-content: center; overflow: hidden; }
  .pic--photo { background: linear-gradient(180deg, #3b3a3f 0%, #d9b6a4 55%, #5b4b4f 100%); }

  .tab-bar {
    position: absolute; left: 0; right: 0; bottom: 0; height: 40px;
    display: flex; font-size: 17px; color: #fff;
  }
  .tab { flex: 1; display: flex; align-items: center; justify-content: center; background: var(--tab-deep); }
  .tab--active { background: var(--tab-pink); justify-content: flex-start; padding-left: 14px; }
</style>
</head>
<body>

<!-- Inbox screen -->
<section class="screen screen--inbox">
  <header class="app-header">
    <div class="brand"><span class="brand-dot"></span>Harborwink</div>
    <div class="nav-item nav-item--active">
      <svg width="30" height="28" viewBox="0 0 30 28"><path d="M15 2 L29 15 H25 V26 H18 V18 H12 V26 H5 V15 H1 Z" fill="#fff"/></svg>
    </div>
    <div class="nav-item nav-item--lit">
      <svg width="32" height="22" viewBox="0 0 32 22"><rect x="1" y="1" width="30" height="20" fill="#fff"/><path d="M1 1 L16 13 L31 1" fill="none" stroke="#2a6d9e" stroke-width="2"/></svg>
    </div>
    <div class="nav-item">
      <svg width="30" height="30" viewBox="0 0 30 30"><circle cx="15" cy="15" r="10" fill="none" stroke="#cfd8e0" stroke-width="5" stroke-dasharray="5 3"/><circle cx="15" cy="15" r="6" fill="none" stroke="#cfd8e0" stroke-width="3"/></svg>
    </div>
  </header>
  <ul class="thread-list">
    <li class="thread">
      <div class="avatar-col"><div class="avatar" role="img" aria-label="Profile photo of Mira Calloway"></div><span class="location">New York, USA</span></div>
      <div class="bubble"><p class="bubble-name"><span class="online-dot"></span>Mira Calloway, <span class="bubble-age">28</span></p><p class="bubble-text">Cool I love it, tonight should be very eventful!</p></div>
    </li>
    <li class="thread">
      <div class="avatar-col"><div class="avatar avatar--blue" role="img" aria-label="Profile photo of Tobi-Tobi"></div><span class="location">Sacramento, USA</span></div>
      <div class="bubble"><p class="bubble-name"><span class="online-dot"></span>Tobi-Tobi, <span class="bubble-age">33</span></p><p class="bubble-text">I hope this design would be chosen. If it does happen then it's cool!</p></div>
    </li>
    <li class="thread">
      <div class="avatar-col"><div class="avatar" role="img" aria-label="Profile photo of Rosalie"></div><span class="location">Chicago, USA</span></div>
      <div class="bubble"><p class="bubble-name"><span class="online-dot"></span>Rosalie, <span class="bubble-age">28</span></p><p class="bubble-text">Hi tobi-tobi how are you. If you win you should treat me for a dinner :)</p></div>
    </li>
    <li class="thread">
      <div class="avatar-col"><div class="avatar" role="img" aria-label="Profile photo of Lanie Sweet"></div></div>
      <div class="bubble"><p class="bubble-name"><span class="online-dot"></span>Lanie Sweet, <span class="bubble-age">3</span></p><p class="bubble-text">Papa, bleeeeeeeee...........</p></div>
    </li>
  </ul>
</section>

<!-- Profile screen -->
<section class="screen screen--profile">
  <div class="status-bar">
    <span class="carrier">
      <svg width="22" height="12" viewBox="0 0 22 12"><rect x="0" y="8" width="3" height="4" fill="#fff"/><rect x="5" y="6" width="3" height="6" fill="#fff"/><rect x="10" y="4" width="3" height="8" fill="#fff"/><rect x="15" y="1" width="3" height="11" fill="#fff"/></svg>3G
    </span>
    <span>9:41 AM</span>
    <span class="battery"></span>
  </div>
  <header class="app-header">
    <div class="brand"><span class="brand-dot"></span>Harborwink</div>
    <div class="nav-item">
      <svg width="30" height="28" viewBox="0 0 30 28"><path d="M15 2 L29 15 H25 V26 H18 V18 H12 V26 H5 V15 H1 Z" fill="#fff"/></svg>
    </div>
    <div class="nav-item">
      <svg width="32" height="22" viewBox="0 0 32 22"><rect x="1" y="1" width="30" height="20" fill="#fff"/><path d="M1 1 L16 13 L31 1" fill="none" stroke="#1f5d8c" stroke-width="2"/></svg>
    </div>
    <div class="nav-item nav-item--lit">
      <svg width="30" height="30" viewBox="0 0 30 30"><circle cx="15" cy="15" r="10" fill="none" stroke="#fff" stroke-width="5" stroke-dasharray="5 3"/><circle cx="15" cy="15" r="6" fill="none" stroke="#fff" stroke-width="3"/></svg>
    </div>
  </header>
  <form class="profile-form">
    <div class="field field--active">Tobi-tobi Ren|</div>
    <div class="field">Email</div>
    <div class="field-row">
      <div class="field field--age">Age</div>
      <div class="field field--sex">Sex <span class="arrow"></span></div>
    </div>
    <div class="field">Height <span class="arrow"></span></div>
    <div class="field">Discovery Range <span class="arrow"></span></div>
    <p class="pics-label">Enter up to 5 pics</p>
    <div class="pic-row">
      <div class="pic pic--photo" role="img" aria-label="Uploaded profile photo"></div>
      <div class="pic"><svg width="70" height="70" viewBox="0 0 70 70"><circle cx="35" cy="24" r="14" fill="#6d6d6d"/><path d="M8 70 C8 48 62 48 62 70 Z" fill="#6d6d6d"/></svg></div>
      <div class="pic"><svg width="70" height="70" viewBox="0 0 70 70"><circle cx="35" cy="24" r="14" fill="#6d6d6d"/><path d="M8 70 C8 48 62 48 62 70 Z" fill="#6d6d6d"/></svg></div>
      <div class="pic"><svg width="70" height="70" viewBox="0 0 70 70"><circle cx="35" cy="24" r="14" fill="#6d6d6d"/><path d="M8 70 C8 48 62 48 62 70 Z" fill="#6d6d6d"/></svg></div>
    </div>
  </form>
  <nav class="tab-bar">
    <div class="tab tab--active">Profile</div>
    <div class="tab">Security</div>
    <div class="tab">Legal</div>
  </nav>
</section>

</body>
</html>
```